Physiotherapy business needs patient information graphic redesign

We have existing graphics that we need redesigned to add some artistic flare. The images must remain professional and suitable for a healthcare setting but some artistic flare is need to add interest to the graphics so that patients are able to engage more easily with the info sheet. Graphics include "INS", "graded activity", "pacing I", "pacing II" and "sleep"

Target Market(s)

Practitioners and patients with pain

Industry/Entity Type

Business

Font styles to use
Sans Serif

Colors
3176b5
9bcb3b
ec1f27

Requirements
Must have
• The ability to communicate the message in the graphic
• Artistic flair
• Retain professionalism
Nice to have
• Unique creativity that distinguishes our product
• Matching with our logo (attached). Does not have to be the same colours or style/font but still should fit with the logo stylistically
Should not have
• A similar boring and flat feel as the existing graphics

```html
<!DOCTYPE html>
<html lang="en">
<head>
<meta charset="utf-8">
<title>Pacing I</title>
<link href="https://fonts.googleapis.com/css2?family=Montserrat:wght@400;700;800&display=swap" rel="stylesheet">
<style>
  :root {
    --brand-blue: #1e84c6;
    --brand-blue-deep: #155f99;
    --brand-blue-light: #4aa6e0;
    --brand-green: #8cc63f;
    --alert-red: #ec1f27;
    --alert-red-deep: #b5121a;
    --grid-blue: #b4cdf0;
    --ink: #111111;
    --marker-grey: #4d5256;
    --page: #ffffff;
    --backdrop: #f1f1f1;
  }
  html, body {
    margin: 0;
    width: 1200px;
    height: 1200px;
    overflow: hidden;
    background: var(--backdrop);
  }
  .sheet {
    position: absolute;
    left: 0;
    top: 137px;
    width: 1200px;
    height: 926px;
    background: var(--page);
  }
  .sheet svg { display: block; width: 100%; height: 100%; }
  .brand-name { font-family: "Montserrat", sans-serif; font-weight: 700; font-size: 28px; fill: var(--brand-blue); letter-spacing: 1px; }
  .title { font-family: "Montserrat", sans-serif; font-weight: 800; font-size: 84px; fill: var(--brand-blue); letter-spacing: 2px; }
  .axis-label { font-family: "Montserrat", sans-serif; font-weight: 700; font-size: 40px; fill: var(--ink); }
  .pin-label { font-family: "Montserrat", sans-serif; font-weight: 400; font-size: 21px; fill: #ffffff; }
  .grid-line { stroke: var(--grid-blue); stroke-width: 1.5; }
  .chart-field { fill: url(#fieldTint); }
  .chart-frame { fill: none; stroke: var(--brand-green); stroke-width: 3; }
  .activity-area { fill: url(#areaTint); }
  .activity-glow { fill: none; stroke: var(--alert-red); stroke-width: 10; stroke-opacity: 0.15; stroke-linejoin: round; }
  .activity-line { fill: none; stroke: url(#lineTone); stroke-width: 3.5; stroke-linejoin: round; }
  .pin-body { fill: url(#pinTone); }
  .pin-icon { fill: url(#iconTone); }
  .pin-dot { fill: var(--marker-grey); stroke: #ffffff; stroke-width: 2; }
  .rule { stroke: var(--brand-green); stroke-width: 2; }
  .footer-band { fill: url(#bandTone); }
</style>
</head>
<body>
<div class="sheet">
  <svg viewBox="0 0 1400 1080" xmlns="http://www.w3.org/2000/svg">
    <defs>
      <radialGradient id="pinTone" cx="0.35" cy="0.3" r="0.8">
        <stop offset="0" stop-color="var(--brand-blue-light)"/>
        <stop offset="0.6" stop-color="var(--brand-blue)"/>
        <stop offset="1" stop-color="var(--brand-blue-deep)"/>
      </radialGradient>
      <linearGradient id="iconTone" x1="0" y1="0" x2="0" y2="1">
        <stop offset="0" stop-color="#ffffff" stop-opacity="0.45"/>
        <stop offset="1" stop-color="#ffffff" stop-opacity="0.12"/>
      </linearGradient>
      <linearGradient id="lineTone" x1="0" y1="0" x2="1" y2="0">
        <stop offset="0" stop-color="var(--alert-red-deep)"/>
        <stop offset="0.5" stop-color="var(--alert-red)"/>
        <stop offset="1" stop-color="var(--alert-red-deep)"/>
      </linearGradient>
      <linearGradient id="areaTint" x1="0" y1="0" x2="0" y2="1">
        <stop offset="0" stop-color="var(--alert-red)" stop-opacity="0.16"/>
        <stop offset="1" stop-color="var(--alert-red)" stop-opacity="0"/>
      </linearGradient>
      <linearGradient id="fieldTint" x1="0" y1="0" x2="0" y2="1">
        <stop offset="0" stop-color="var(--brand-green)" stop-opacity="0.10"/>
        <stop offset="0.55" stop-color="#ffffff" stop-opacity="0"/>
        <stop offset="1" stop-color="var(--brand-blue)" stop-opacity="0.08"/>
      </linearGradient>
      <linearGradient id="bandTone" x1="0" y1="0" x2="1" y2="0">
        <stop offset="0" stop-color="var(--brand-blue-deep)"/>
        <stop offset="0.7" stop-color="var(--brand-blue)"/>
        <stop offset="1" stop-color="var(--brand-green)"/>
      </linearGradient>
      <filter id="softShadow" x="-30%" y="-30%" width="160%" height="170%">
        <feDropShadow dx="0" dy="5" stdDeviation="5" flood-color="#0b3d66" flood-opacity="0.3"/>
      </filter>
    </defs>

    <!-- brand -->
    <circle cx="94" cy="96" r="24" fill="var(--brand-green)"/>
    <text class="brand-name" x="134" y="92">STRIDE</text>
    <text class="brand-name" x="134" y="122">HEALTHCARE</text>
    <line class="rule" x1="382" y1="119" x2="1400" y2="119"/>
    <text class="title" x="890" y="103" text-anchor="middle">PACING I</text>

    <!-- axis labels -->
    <text class="axis-label" x="141" y="370" text-anchor="middle">Normal</text>
    <text class="axis-label" x="141" y="421" text-anchor="middle">Activity</text>
    <text class="axis-label" x="143" y="760" text-anchor="middle">Under</text>
    <text class="axis-label" x="143" y="811" text-anchor="middle">Activity</text>

    <!-- chart field and grid -->
    <rect class="chart-field" x="262" y="309" width="1046" height="584"/>
    <g class="grid">
      <line class="grid-line" x1="323.5" y1="309" x2="323.5" y2="893"/>
      <line class="grid-line" x1="385" y1="309" x2="385" y2="893"/>
      <line class="grid-line" x1="446.5" y1="309" x2="446.5" y2="893"/>
      <line class="grid-line" x1="508" y1="309" x2="508" y2="893"/>
      <line class="grid-line" x1="569.5" y1="309" x2="569.5" y2="893"/>
      <line class="grid-line" x1="631" y1="309" x2="631" y2="893"/>
      <line class="grid-line" x1="692.5" y1="309" x2="692.5" y2="893"/>
      <line class="grid-line" x1="754" y1="309" x2="754" y2="893"/>
      <line class="grid-line" x1="815.5" y1="309" x2="815.5" y2="893"/>
      <line class="grid-line" x1="877" y1="309" x2="877" y2="893"/>
      <line class="grid-line" x1="938.5" y1="309" x2="938.5" y2="893"/>
      <line class="grid-line" x1="1000" y1="309" x2="1000" y2="893"/>
      <line class="grid-line" x1="1061.5" y1="309" x2="1061.5" y2="893"/>
      <line class="grid-line" x1="1123" y1="309" x2="1123" y2="893"/>
      <line class="grid-line" x1="1184.5" y1="309" x2="1184.5" y2="893"/>
      <line class="grid-line" x1="1246" y1="309" x2="1246" y2="893"/>
      <line class="grid-line" x1="262" y1="362" x2="1308" y2="362"/>
      <line class="grid-line" x1="262" y1="415" x2="1308" y2="415"/>
      <line class="grid-line" x1="262" y1="468" x2="1308" y2="468"/>
      <line class="grid-line" x1="262" y1="521" x2="1308" y2="521"/>
      <line class="grid-line" x1="262" y1="574" x2="1308" y2="574"/>
      <line class="grid-line" x1="262" y1="627" x2="1308" y2="627"/>
      <line class="grid-line" x1="262" y1="680" x2="1308" y2="680"/>
      <line class="grid-line" x1="262" y1="733" x2="1308" y2="733"/>
      <line class="grid-line" x1="262" y1="786" x2="1308" y2="786"/>
      <line class="grid-line" x1="262" y1="839" x2="1308" y2="839"/>
    </g>
    <rect class="chart-frame" x="262" y="309" width="1046" height="584" rx="6"/>

    <!-- activity trace -->
    <polygon class="activity-area" points="461,732 528,422 600,732 718,732 784,422 856,735 981,735 1048,422 1123,732"/>
    <polyline class="activity-glow" points="322,732 461,732 528,422 600,732 718,732 784,422 856,735 981,735 1048,422 1123,732 1244,732"/>
    <polyline class="activity-line" points="322,732 461,732 528,422 600,732 718,732 784,422 856,735 981,735 1048,422 1123,732 1244,732"/>

    <!-- overdo markers -->
    <g class="pin pin-overdo" filter="url(#softShadow)">
      <path class="pin-body" d="M513,377 A73,73 0 1 1 543,377 L528,418 Z"/>
      <rect class="pin-icon" x="488" y="260" width="80" height="64" rx="14" role="img" aria-label="Icon of a person sitting up in bed beside a sunrise window"/>
      <text class="pin-label" x="528" y="345" text-anchor="middle">Overdo</text>
      <text class="pin-label" x="528" y="367" text-anchor="middle">Activity</text>
    </g>
    <circle class="pin-dot" cx="528" cy="422" r="9"/>
    <g class="pin pin-overdo" filter="url(#softShadow)">
      <path class="pin-body" d="M769,377 A73,73 0 1 1 799,377 L784,418 Z"/>
      <rect class="pin-icon" x="744" y="260" width="80" height="64" rx="14" role="img" aria-label="Icon of a person sitting up in bed beside a sunrise window"/>
      <text class="pin-label" x="784" y="345" text-anchor="middle">Overdo</text>
      <text class="pin-label" x="784" y="367" text-anchor="middle">Activity</text>
    </g>
    <circle class="pin-dot" cx="784" cy="422" r="9"/>
    <g class="pin pin-overdo" filter="url(#softShadow)">
      <path class="pin-body" d="M1033,377 A73,73 0 1 1 1063,377 L1048,418 Z"/>
      <rect class="pin-icon" x="1008" y="260" width="80" height="64" rx="14" role="img" aria-label="Icon of a person sitting up in bed beside a sunrise window"/>
      <text class="pin-label" x="1048" y="345" text-anchor="middle">Overdo</text>
      <text class="pin-label" x="1048" y="367" text-anchor="middle">Activity</text>
    </g>
    <circle class="pin-dot" cx="1048" cy="422" r="9"/>

    <!-- rest markers -->
    <g class="pin pin-rest" filter="url(#softShadow)">
      <path class="pin-body" d="M642,687 A66,66 0 1 1 670,687 L656,726 Z"/>
      <rect class="pin-icon" x="614" y="596" width="86" height="46" rx="14" role="img" aria-label="Icon of a person lying down asleep in bed"/>
      <text class="pin-label" x="656" y="667" text-anchor="middle">Rest</text>
    </g>
    <circle class="pin-dot" cx="656" cy="730" r="9"/>
    <g class="pin pin-rest" filter="url(#softShadow)">
      <path class="pin-body" d="M902,687 A66,66 0 1 1 930,687 L916,728 Z"/>
      <rect class="pin-icon" x="874" y="596" width="86" height="46" rx="14" role="img" aria-label="Icon of a person lying down asleep in bed"/>
      <text class="pin-label" x="916" y="667" text-anchor="middle">Rest</text>
    </g>
    <circle class="pin-dot" cx="916" cy="733" r="9"/>

    <!-- footer band -->
    <rect class="footer-band" x="0" y="1047" width="1400" height="33"/>
  </svg>
</div>
</body>
</html>
```